Maplecrest Insurance Services - Application Designs

My company name is Maplecrest Insurance Services. We are a full service insurance brokerage.

I need an ACH Form (which is attached) to be created with my logo (which is also attached). Please make the ACH Form fillable for info to be entered manually.

In addition I need the Example Quote created with the same color scheme as the Maplecrest Logo. Please create the Example quote as a word document so I can edit the quote and save as a PDF. You can also send me different quote ideas as long as they have the same information on the quote I have attached.

For the Example Supplemental you can leave everything as is and just change the Tillmoor Logo to the attached Maplecrest Insurance Services Logo.

- Change all color-ways to the Maplecrest Insurance Services color-way logo
- Change all the Tillmoor logos to the Maplecrest logo
- Phone number to the company is (555) 317-2096
- Change anything that says Tillmoor to Maplecrest
- Company address is: 7810 Pellway Ave, Unit D Studio City CA 91604
- Company Email address is Dana@Maplecrestinsuranceservices.example

Target Market(s)

Clients or Potential Clients

Industry/Entity Type

Insurance

Font styles to use
Serif

Colors
0054AA
0677BA
7BADD7
CADEEF
E8F1F8
00AB8E
00BBA5
67D7C9
C6EFE9
E9F9F6

Requirements
Must have
• Maplecrest Insurance Services Logo

```html
<!DOCTYPE html>
<html lang="en">
<head>
<meta charset="utf-8">
<title>Maplecrest Insurance Services – Supplemental Application</title>
<link href="https://fonts.googleapis.com/css2?family=Arimo:wght@400;700&display=swap" rel="stylesheet">
<style>
:root{
  --navy:#0054AA;
  --blue:#0677BA;
  --sky:#7BADD7;
  --mist:#CADEEF;
  --ice:#E8F1F8;
  --green:#00AB8E;
  --teal:#00BBA5;
  --ink:#1c1c1c;
  --rule:#8a8a8a;
  --canvas:#eeeeee;
  --paper:#ffffff;
}
*{box-sizing:border-box;margin:0;padding:0}
html,body{width:1200px;height:2400px;overflow:hidden;background:var(--canvas);font-family:"Arimo",Arial,sans-serif;color:var(--ink)}
.page{position:absolute;left:80px;width:1040px;height:1130px;background:var(--paper);box-shadow:0 2px 10px rgba(0,0,0,.22);padding:36px 70px 0}
.page-one{top:35px}
.page-two{top:1230px}
.brand{display:flex;justify-content:center;align-items:center;gap:14px;height:78px;margin-bottom:20px}
.brand-dot{width:22px;height:22px;border-radius:50%;background:var(--green)}
.brand-name{font-size:30px;font-weight:700;color:var(--navy);letter-spacing:.5px}
.fill-line{display:flex;align-items:flex-end;font-size:12px;font-weight:700;height:20px;margin-bottom:4px}
.fill-line .blank{flex:1;border-bottom:1px solid var(--ink);margin:0 10px 2px 6px}
.fill-line .short{flex:0 0 230px}
.note{font-size:11px;font-weight:700;margin:6px 0 8px}
.payroll{width:100%;border-collapse:collapse;font-size:11px;margin-bottom:26px}
.payroll th,.payroll td{border:1px solid var(--rule);height:19px;padding:0 6px;text-align:left}
.payroll th{font-weight:700;text-align:center;background:var(--ice)}
.payroll td:first-child{width:140px}
.section-title{font-size:12px;font-weight:700;color:var(--navy);border-bottom:2px solid var(--navy);padding-bottom:2px;margin-bottom:0;text-transform:uppercase}
.section{margin-bottom:24px}
.row{display:grid;grid-template-columns:3fr 1.1fr 3fr 1.1fr;font-size:10.5px;border-bottom:1px solid var(--rule);border-left:1px solid var(--rule)}
.row>span{height:20px;line-height:20px;padding:0 5px;border-right:1px solid var(--rule);white-space:nowrap;overflow:hidden}
.row.full{grid-template-columns:6.2fr 1.1fr 1fr}
.row.text{grid-template-columns:3fr 4.2fr}
.answer{display:flex;align-items:center;gap:4px}
.box{display:inline-block;width:10px;height:10px;border:1px solid var(--ink);margin-left:4px}
.desc-line{height:20px;border-bottom:1px solid var(--rule);border-left:1px solid var(--rule);border-right:1px solid var(--rule);font-size:10.5px;padding:3px 5px}
.footer{position:absolute;left:70px;right:70px;bottom:26px;border-top:3px solid var(--navy);display:flex;justify-content:space-between;font-size:10px;padding-top:5px}
.footer::before{content:"";position:absolute;left:0;top:-7px;width:140px;height:3px;background:var(--green)}
.footer .num{flex:1;text-align:center}
</style>
</head>
<body>

<section class="page page-one">
  <header class="brand"><span class="brand-dot"></span><span class="brand-name">MAPLECREST INSURANCE SERVICES</span></header>

  <div class="fill-line">Insured Name:<span class="blank"></span></div>
  <div class="fill-line">Web Site:<span class="blank"></span>FEIN:<span class="blank short"></span></div>
  <p class="note">Applicant must complete page 1, 2 and the sections pertinent</p>

  <table class="payroll">
    <tr><th></th><th>Payroll Information</th><th>Premium Information</th></tr>
    <tr><td>Current Year</td><td></td><td></td></tr>
    <tr><td>Prior Year</td><td></td><td></td></tr>
    <tr><td>Prior Year</td><td></td><td></td></tr>
    <tr><td>Prior Year</td><td></td><td></td></tr>
    <tr><td>Prior Year</td><td></td><td></td></tr>
  </table>

  <div class="section">
    <h2 class="section-title">Operational Information</h2>
    <div class="desc-line">Description of operations for all proposed classes (list):</div>
    <div class="desc-line"></div>
    <div class="desc-line"></div>
    <div class="row"><span>Hours of operation</span><span></span><span>Any 24 hr shifts?</span><span class="answer"><i class="box"></i>Yes<i class="box"></i>No</span></div>
    <div class="row"><span># of years in business</span><span></span><span>Average employee tenure</span><span></span></div>
    <div class="row full"><span>Have you ever filed for bankruptcy within the past 7 years?</span><span class="answer"><i class="box"></i>Yes</span><span class="answer"><i class="box"></i>No</span></div>
  </div>

  <div class="section">
    <h2 class="section-title">Safety Information</h2>
    <div class="row"><span>Active EPP</span><span class="answer"><i class="box"></i>Yes<i class="box"></i>No</span><span>Written ownership in operations</span><span class="answer"><i class="box"></i>Yes<i class="box"></i>No</span></div>
    <div class="row"><span>Written safety program</span><span class="answer"><i class="box"></i>Yes<i class="box"></i>No</span><span>Personal protective equipment</span><span class="answer"><i class="box"></i>Yes<i class="box"></i>No</span></div>
    <div class="row"><span>Respirator program</span><span class="answer"><i class="box"></i>Yes<i class="box"></i>No</span><span>If yes, type of PPE</span><span></span></div>
    <div class="row"><span>Safety incentives</span><span class="answer"><i class="box"></i>Yes<i class="box"></i>No</span><span>Formal return to work program</span><span class="answer"><i class="box"></i>Yes<i class="box"></i>No</span></div>
    <div class="row"><span>Monthly safety meetings</span><span class="answer"><i class="box"></i>Yes<i class="box"></i>No</span><span>Light duty available</span><span class="answer"><i class="box"></i>Yes<i class="box"></i>No</span></div>
    <div class="row"><span>Frequency of written safety audits</span><span></span><span>Drug testing program</span><span class="answer"><i class="box"></i>Yes<i class="box"></i>No</span></div>
    <div class="row"><span>% of bilingual employees</span><span></span><span>Language of training</span><span class="answer"><i class="box"></i>Eng<i class="box"></i>Span</span></div>
    <div class="row"><span>Safety manual</span><span class="answer"><i class="box"></i>Yes<i class="box"></i>No</span><span>Training records kept</span><span class="answer"><i class="box"></i>Yes<i class="box"></i>No</span></div>
    <div class="row"><span>Full-time manager employed</span><span class="answer"><i class="box"></i>Yes<i class="box"></i>No</span><span>Site inspections performed</span><span class="answer"><i class="box"></i>Yes<i class="box"></i>No</span></div>
    <div class="row"><span>Do supervisors receive specific training</span><span class="answer"><i class="box"></i>Yes<i class="box"></i>No</span><span>Inspection frequency</span><span></span></div>
    <div class="row"><span>Supervisor held accountable</span><span class="answer"><i class="box"></i>Yes<i class="box"></i>No</span><span>Fall protection used</span><span class="answer"><i class="box"></i>Yes<i class="box"></i>No</span></div>
    <div class="row"><span>Number of employees trained</span><span></span><span>Ladders inspected</span><span class="answer"><i class="box"></i>Yes<i class="box"></i>No</span></div>
    <div class="row"><span>Accident investigation process</span><span class="answer"><i class="box"></i>Yes<i class="box"></i>No</span><span>Lockout tagout program</span><span class="answer"><i class="box"></i>Yes<i class="box"></i>No</span></div>
    <div class="row"><span>Written safety rules enforced</span><span class="answer"><i class="box"></i>Yes<i class="box"></i>No</span><span>Confined space entry</span><span class="answer"><i class="box"></i>Yes<i class="box"></i>No</span></div>
    <div class="row"><span>Written disciplinary policy/procedure</span><span class="answer"><i class="box"></i>Yes<i class="box"></i>No</span><span>Forklift certification</span><span class="answer"><i class="box"></i>Yes<i class="box"></i>No</span></div>
    <div class="row"><span>Medical facility designated</span><span class="answer"><i class="box"></i>Yes<i class="box"></i>No</span><span>Equipment maintained</span><span class="answer"><i class="box"></i>Yes<i class="box"></i>No</span></div>
    <div class="row"><span>Modified duty program in place</span><span class="answer"><i class="box"></i>Yes<i class="box"></i>No</span><span>First aid kits on site</span><span class="answer"><i class="box"></i>Yes<i class="box"></i>No</span></div>
    <div class="row"><span>Injury log maintained</span><span class="answer"><i class="box"></i>Yes<i class="box"></i>No</span><span>Claims reviewed monthly</span><span class="answer"><i class="box"></i>Yes<i class="box"></i>No</span></div>
    <div class="row full"><span>Is training provided to new hires and existing employees on proper use and maintenance of equipment?</span><span class="answer"><i class="box"></i>Yes</span><span class="answer"><i class="box"></i>No</span></div>
    <div class="row full"><span>Are all employees that operate forklifts licensed or certified?</span><span class="answer"><i class="box"></i>Yes</span><span class="answer"><i class="box"></i>No</span></div>
    <div class="row full"><span>Has your company implemented any ergonomic safety procedures?</span><span class="answer"><i class="box"></i>Yes</span><span class="answer"><i class="box"></i>No</span></div>
    <div class="row"><span>Monthly equipment check</span><span class="answer"><i class="box"></i>Yes<i class="box"></i>No</span><span>Standard for reports</span><span class="answer"><i class="box"></i>Yes<i class="box"></i>No</span></div>
  </div>

  <footer class="footer"><span></span><span class="num">1</span><span>REV 01/24</span></footer>
</section>

<section class="page page-two">
  <header class="brand"><span class="brand-dot"></span><span class="brand-name">MAPLECREST INSURANCE SERVICES</span></header>

  <div class="section">
    <h2 class="section-title">Employment Practices</h2>
    <div class="row"><span>Written employment contract</span><span class="answer"><i class="box"></i>Yes<i class="box"></i>No</span><span>Currently in EPPL</span><span class="answer"><i class="box"></i>Yes<i class="box"></i>No</span></div>
    <div class="row"><span>Percentage of employees enrolled</span><span></span><span>Number of full time employees</span><span></span></div>
    <div class="row"><span>Percentage paid by employees</span><span></span><span>Number of part time employees</span><span></span></div>
    <div class="row"><span>Disability insurance provided</span><span class="answer"><i class="box"></i>Yes<i class="box"></i>No</span><span>Number of seasonal employees</span><span></span></div>
    <div class="row"><span>Paid sick leave provided</span><span class="answer"><i class="box"></i>Yes<i class="box"></i>No</span><span>Number of clerical workers</span><span></span></div>
    <div class="row"><span>Retirement plan offered</span><span class="answer"><i class="box"></i>Yes<i class="box"></i>No</span><span>Employees length of service</span><span></span></div>
    <div class="row"><span>Do you lease workers</span><span class="answer"><i class="box"></i>Yes<i class="box"></i>No</span><span>Number of leased workers</span><span></span></div>
    <div class="row"><span>Union employees</span><span class="answer"><i class="box"></i>Yes<i class="box"></i>No</span><span>Employees hired each year</span><span></span></div>
    <div class="row"><span>Pay frequency</span><span class="answer"><i class="box"></i>Wk<i class="box"></i>Mo</span><span>Employees terminated each year</span><span></span></div>
    <div class="row"><span>Do you use temporary labor</span><span class="answer"><i class="box"></i>Yes<i class="box"></i>No</span><span>Average hourly wage</span><span></span></div>
    <div class="row"><span>Have you been audited in the past year</span><span class="answer"><i class="box"></i>Yes<i class="box"></i>No</span><span>Overtime worked</span><span class="answer"><i class="box"></i>Yes<i class="box"></i>No</span></div>
    <div class="row full"><span>Do you have an established method for reporting injuries?</span><span class="answer"><i class="box"></i>Yes</span><span class="answer"><i class="box"></i>No</span></div>
  </div>

  <div class="section">
    <h2 class="section-title">Risk Characteristics</h2>
    <div class="row"><span>Vehicles used in business</span><span class="answer"><i class="box"></i>Yes<i class="box"></i>No</span><span>Are employees provided vehicles</span><span class="answer"><i class="box"></i>Yes<i class="box"></i>No</span></div>
    <div class="row"><span>Energy delivery operations</span><span class="answer"><i class="box"></i>Yes<i class="box"></i>No</span><span>Employees use personal vehicles for work</span><span class="answer"><i class="box"></i>Yes<i class="box"></i>No</span></div>
    <div class="row"><span>Purpose of driving operations</span><span></span><span>Uses a device? Ring used in 5 mile radius</span><span class="answer"><i class="box"></i>Yes<i class="box"></i>No</span></div>
    <div class="row"><span>Radius of operations</span><span class="answer"><i class="box"></i>0–25 mi</span><span>Lifting equipment</span><span class="answer"><i class="box"></i>Yes<i class="box"></i>No</span></div>
    <div class="row"><span></span><span class="answer"><i class="box"></i>26–50 mi</span><span>Heavy lifting</span><span class="answer"><i class="box"></i>Yes<i class="box"></i>No</span></div>
    <div class="row"><span></span><span class="answer"><i class="box"></i>51–100 mi</span><span>Work at height</span><span class="answer"><i class="box"></i>Yes<i class="box"></i>No</span></div>
    <div class="row"><span></span><span class="answer"><i class="box"></i>101–200 mi</span><span>Work below ground</span><span class="answer"><i class="box"></i>Yes<i class="box"></i>No</span></div>
    <div class="row"><span></span><span class="answer"><i class="box"></i>200+ mi</span><span>Work over water</span><span class="answer"><i class="box"></i>Yes<i class="box"></i>No</span></div>
    <div class="row"><span>Hours driven weekly</span><span></span><span>Out of state travel or job sites</span><span class="answer"><i class="box"></i>Yes<i class="box"></i>No</span></div>
    <div class="row text"><span>Are driver acceptability standards in place?</span><span></span></div>
    <div class="row"><span>Number of vehicles used</span><span></span><span>Number of authorized drivers</span><span></span></div>
    <div class="row"><span>Frequency of driving reviews</span><span class="answer"><i class="box"></i>Yearly</span><span>Motor vehicle records checked</span><span class="answer"><i class="box"></i>Yes<i class="box"></i>No</span></div>
    <div class="row"><span>Do group transportation to or from work sites</span><span class="answer"><i class="box"></i>Yes<i class="box"></i>No</span><span>Average trip length</span><span></span></div>
    <div class="row text"><span>Number of employees with travel duties</span><span></span></div>
    <div class="row text"><span>Average frequency of trips per year per employee</span><span></span></div>
  </div>

  <div class="section">
    <h2 class="section-title">Employee Selection/ Training/ Qualifications</h2>
    <div class="row"><span>Written application</span><span class="answer"><i class="box"></i>Yes<i class="box"></i>No</span><span>Current job description on file</span><span class="answer"><i class="box"></i>Yes<i class="box"></i>No</span></div>
    <div class="row"><span>Reference check</span><span class="answer"><i class="box"></i>Yes<i class="box"></i>No</span><span>Employee orientation</span><span class="answer"><i class="box"></i>Yes<i class="box"></i>No</span></div>
    <div class="row"><span>Pre-hire drug testing</span><span class="answer"><i class="box"></i>Yes<i class="box"></i>No</span><span>Physical ability test provided</span><span class="answer"><i class="box"></i>Yes<i class="box"></i>No</span></div>
    <div class="row"><span>Post-accident drug testing</span><span class="answer"><i class="box"></i>Yes<i class="box"></i>No</span><span>Documentation used</span><span class="answer"><i class="box"></i>Yes<i class="box"></i>No</span></div>
    <div class="row"><span>Random drug testing</span><span class="answer"><i class="box"></i>Yes<i class="box"></i>No</span><span>If yes, date of last check</span><span></span></div>
    <div class="row"><span>Position testing (physical)</span><span class="answer"><i class="box"></i>Yes<i class="box"></i>No</span><span>Skills assessment</span><span class="answer"><i class="box"></i>Yes<i class="box"></i>No</span></div>
    <div class="row full"><span>Describe any other physical or assessment tests conducted prior to placement:</span><span></span><span></span></div>
    <div class="row"><span>Criminal background check</span><span class="answer"><i class="box"></i>Yes<i class="box"></i>No</span><span>Level of clearance</span><span></span></div>
    <div class="row full"><span>Are new hires subject to a probationary period before full duties?</span><span class="answer"><i class="box"></i>Yes</span><span class="answer"><i class="box"></i>No</span></div>
    <div class="row full"><span>Does the company require all workers to complete annual training?</span><span class="answer"><i class="box"></i>Yes</span><span class="answer"><i class="box"></i>No</span></div>
    <div class="row full"><span>If yes, please list what training is provided:</span><span></span><span></span></div>
  </div>

  <footer class="footer"><span></span><span class="num">2</span><span>REV 01/24</span></footer>
</section>

</body>
</html>
```